Buch-/eBook-Cover für populär-wissenschaftliches Buch
Zielgruppe
Der Talgrund-Verlag veröffentlicht Bücher zu psychologischen Themen. Dies ist ein eher populär wissenschaftliches Buch für eine breite Leserschaft.
Aufgabenstellung
Benötigt wird ein Buchcover für KTZ, Papierformat 158*223, Buchformat 154 x 3 x 217 mm 272 Normseiten
Kurzbeschreibung
Am Ufer getragen?
Fragen sich die Autoren Konrad Brüning und Matthias Oswerk. Zwei Psychoanalytiker mit langer Berufserfahrung. Geht das überhaupt: in Liebe und vereint zu sein? Dazu müssen zunächst andere Fragen geklärt werden.
Was vereint die Geschlechter, was bringt sie zusammen? Liebe? Dieses Wort gab es im Deutschen im frühen Mittelalter nicht, erst im späteren. In manchen Kulturen gibt es dieses Wort bis heute nicht, und dennoch leben Mann und Frau zusammen. Schon seit Jahrtausenden beschäftigt sich der Mensch mit der Beziehung zwischen den Geschlechtern. Philosophen, Schriftsteller, Dichter, Maler, Musiker, später Psychoanalytiker, Anthropologen und Soziologen hat die Beziehung zwischen Mann und Frau intensiv beschäftigt. Auch die Religionen befassen sich mit der Beziehung zwischen den Geschlechtern und zeigen vorwiegend auf moralischen und idealistischen Ebenen Umgangsweisen und Lebensformen zwischen den Geschlechtern auf.
280 Normseiten
Bitte Klappentext auf Rückseite

```html
<!DOCTYPE html>
<html lang="de">
<head>
<meta charset="utf-8">
<title>Am Ufer getragen? – Buchcover</title>
<link rel="stylesheet" href="https://fonts.googleapis.com/css2?family=Della+Respira&family=Roboto+Condensed:wght@500&display=swap">
<style>
  :root {
    --cover-bg: #5b1b1e;
    --type-light: #ffffff;
    --tone-amber: #f0891a;
    --tone-teal: #07627a;
    --tone-vermilion: #e4441e;
  }
  html, body {
    margin: 0;
    padding: 0;
    overflow: hidden;
    background: var(--cover-bg);
  }
  .cover {
    position: relative;
    width: 852px;
    height: 1200px;
    overflow: hidden;
    background: var(--cover-bg);
  }
  .cover__authors {
    position: absolute;
    top: 46px;
    left: 0;
    width: 100%;
    margin: 0;
    text-align: center;
    font-family: "Roboto Condensed", "Arial Narrow", sans-serif;
    font-weight: 500;
    font-size: 29px;
    letter-spacing: 0.5px;
    color: var(--type-light);
    text-transform: uppercase;
  }
  .cover__title {
    position: absolute;
    top: 0;
    left: 0;
    width: 852px;
    height: 520px;
    margin: 0;
  }
  .cover__title text {
    font-family: "Della Respira", Georgia, serif;
    font-size: 200px;
    fill: var(--type-light);
  }
  .cover__artwork {
    position: absolute;
    left: 52px;
    top: 548px;
    width: 764px;
    height: 652px;
    border-radius: 260px 260px 0 0;
    background: linear-gradient(90deg,
      var(--tone-amber) 0%,
      var(--tone-amber) 42%,
      var(--tone-teal) 52%,
      var(--tone-vermilion) 62%,
      var(--tone-vermilion) 100%);
  }
</style>
</head>
<body>
  <main class="cover">
    <p class="cover__authors">Konrad Brüning &amp; Matthias Oswerk</p>
    <svg class="cover__title" viewBox="0 0 852 520" role="heading" aria-level="1" aria-label="Am Ufer getragen?">
      <text x="398" y="286" text-anchor="middle" textLength="600" lengthAdjust="spacingAndGlyphs">AM UFER</text>
      <text x="420" y="478" text-anchor="middle" textLength="645" lengthAdjust="spacingAndGlyphs">GETRAGEN?</text>
    </svg>
    <div class="cover__artwork" role="img" aria-label="Illustration: zwei einander abgewandte Kopfsilhouetten in Orange und Rot, die sich in einer blaugrünen Fläche überschneiden"></div>
  </main>
</body>
</html>
```